Additional Benefits of Working for VALMIRA

Please prepare an infographic on the additional benefits besides salary of working at VALMIRA as detailed in the attached word document. Also attached is our logo in eps and our company design "Grounds". We are a Not For Profit company that finds jobs for unemployed people of government benefit payments

Target Market(s)

Attracting people to work for VALMIRA. Making VALMIRA an employer of choice.

Font styles to use
Sans Serif

Colors

Designer to choose colors to be used in the design.

Requirements
Must have
• be on 1 page
• have our logo
Nice to have
• Our Grounds design worked into it.
• Happy engaged employees
• Community engagement - we are a not for profit organisation
Should not have
• Discrimination, swearing,

```html
<!DOCTYPE html>
<html lang="en">
<head>
<meta charset="utf-8">
<title>Benefits of Working with Us – VALMIRA</title>
<link href="https://fonts.googleapis.com/css2?family=Montserrat:wght@500;600;700;800&display=swap" rel="stylesheet">
<style>
  :root {
    --page: #ffffff;
    --ground-grey: #8c9591;
    --ground-mint: #9fcbb3;
    --ground-sand: #e3bf8c;
    --teal: #0f7a5e;
    --teal-dark: #0b5d47;
    --teal-line: #0e6e55;
    --gold: #d99a3e;
    --gold-light: #f4c986;
    --gold-dark: #b9782a;
    --title-gold: #f0c27c;
    --ink: #1b1b1b;
    --white: #ffffff;
  }
  * { box-sizing: border-box; margin: 0; padding: 0; }
  html, body { width: 1200px; height: 990px; overflow: hidden; background: var(--page); }
  body { font-family: "Montserrat", sans-serif; color: var(--ink); position: relative; }

  .poster {
    position: absolute; left: 110px; top: 40px; width: 980px; height: 910px;
    overflow: hidden;
    box-shadow: 6px 6px 8px rgba(0,0,0,.35);
  }
  .grounds-art {
    position: absolute; inset: 0;
    background:
      radial-gradient(ellipse 40% 55% at 55% 75%, rgba(227,191,140,.75), transparent 70%),
      radial-gradient(ellipse 35% 40% at 15% 20%, rgba(159,203,179,.8), transparent 70%),
      radial-gradient(ellipse 40% 35% at 90% 85%, rgba(159,203,179,.7), transparent 70%),
      linear-gradient(135deg, #95a49d 0%, var(--ground-grey) 50%, #97aaa0 100%);
  }

  .brand {
    position: absolute; left: 14px; top: 9px; width: 254px; height: 120px;
    background: var(--white); border-radius: 50%;
    display: flex; align-items: center; justify-content: center;
  }
  .brand-name { font-weight: 800; font-size: 44px; letter-spacing: -1px; color: var(--ink); }

  .headline {
    position: absolute; left: 310px; top: 23px; width: 627px; height: 85px;
    border-radius: 20px;
    background: linear-gradient(180deg, #17a07b 0%, var(--teal) 55%, var(--teal-dark) 100%);
    display: flex; align-items: center; justify-content: center;
    color: var(--title-gold); font-weight: 600; font-size: 40px;
  }

  .links { position: absolute; inset: 0; }

  .icon-badge {
    position: absolute; width: 94px; height: 94px; border-radius: 50%;
    background: var(--white); border: 4px solid var(--teal);
    display: flex; align-items: center; justify-content: center;
  }
  .icon-badge svg { width: 58px; height: 58px; fill: none; stroke: var(--teal); stroke-width: 2.4; stroke-linecap: round; stroke-linejoin: round; }

  .card {
    position: absolute; background: var(--white);
    border: 5px solid var(--gold); border-radius: 20px; overflow: hidden;
  }
  .card-title {
    background: linear-gradient(180deg, var(--gold-light) 0%, var(--gold) 55%, var(--gold-dark) 100%);
    color: var(--teal); font-weight: 500; font-size: 18px; line-height: 1.1;
    text-align: center; padding: 6px 4px;
  }
  .card-list { list-style: none; padding: 6px 8px 0; }
  .card-list li {
    font-size: 10.6px; line-height: 1.3; margin-bottom: 5px; text-align: justify; font-weight: 500;
  }
  .card-list li::before { content: "• "; }
</style>
</head>
<body>
<main class="poster">
  <div class="grounds-art" role="img" aria-label="Grounds company artwork: flowing organic shapes in grey, mint green and sand"></div>

  <div class="brand"><span class="brand-name">valmira</span></div>
  <h1 class="headline">Benefits of Working with Us</h1>

  <svg class="links" viewBox="0 0 980 910" aria-hidden="true">
    <g stroke="var(--teal-line)" stroke-width="5" fill="none">
      <line x1="140" y1="162" x2="832" y2="162"/>
      <line x1="140" y1="563" x2="832" y2="563"/>
      <line x1="832" y1="175" x2="832" y2="574"/>
      <line x1="140" y1="513" x2="140" y2="574"/>
      <line x1="360" y1="484" x2="360" y2="574"/>
      <line x1="598" y1="507" x2="598" y2="574"/>
      <line x1="140" y1="574" x2="140" y2="651"/>
      <line x1="360" y1="574" x2="360" y2="649"/>
      <line x1="598" y1="574" x2="598" y2="651"/>
      <line x1="832" y1="574" x2="832" y2="650"/>
    </g>
  </svg>

  <!-- Row one icons -->
  <div class="icon-badge" style="left:93px;top:128px">
    <svg viewBox="0 0 48 48"><line x1="24" y1="6" x2="24" y2="40"/><line x1="10" y1="12" x2="38" y2="12"/><path d="M10 12 4 26h12z"/><path d="M38 12 32 26h12z"/><path d="M4 26a6 4 0 0 0 12 0"/><path d="M32 26a6 4 0 0 0 12 0"/><line x1="16" y1="42" x2="32" y2="42"/><circle cx="24" cy="6" r="2"/></svg>
  </div>
  <div class="icon-badge" style="left:313px;top:128px">
    <svg viewBox="0 0 48 48"><path d="M24 40 8 24a9 9 0 0 1 16-11 9 9 0 0 1 16 11z"/><path d="M24 34 12 22a5 5 0 0 1 12-6 5 5 0 0 1 12 6z"/></svg>
  </div>
  <div class="icon-badge" style="left:551px;top:128px">
    <svg viewBox="0 0 48 48"><path d="M6 6v36h36"/><line x1="12" y1="40" x2="12" y2="30"/><line x1="18" y1="40" x2="18" y2="26"/><line x1="24" y1="40" x2="24" y2="30"/><line x1="30" y1="40" x2="30" y2="22"/><line x1="36" y1="40" x2="36" y2="16"/><path d="M10 28l10-10 6 6 14-14"/><path d="M34 10h6v6"/></svg>
  </div>
  <div class="icon-badge" style="left:785px;top:128px">
    <svg viewBox="0 0 48 48"><rect x="10" y="8" width="28" height="34" rx="3"/><path d="M10 14h28"/><rect x="26" y="22" width="12" height="10" rx="2"/><circle cx="31" cy="27" r="1.5"/></svg>
  </div>

  <!-- Row two icons -->
  <div class="icon-badge" style="left:93px;top:527px">
    <svg viewBox="0 0 48 48"><circle cx="24" cy="24" r="18"/><path d="M10 18c5 0 6 4 10 4s3 6 0 8-2 8-2 10"/><path d="M28 8c-2 4 2 6 6 6s4 6 8 6"/><path d="M30 28c2 2 6 2 8 6"/></svg>
  </div>
  <div class="icon-badge" style="left:313px;top:527px">
    <svg viewBox="0 0 48 48"><path d="M4 8h6l6 24h22l5-16H12"/><line x1="20" y1="20" x2="36" y2="20"/><line x1="22" y1="26" x2="34" y2="26"/><circle cx="19" cy="40" r="3"/><circle cx="35" cy="40" r="3"/></svg>
  </div>
  <div class="icon-badge" style="left:551px;top:527px">
    <svg viewBox="0 0 48 48"><path d="M16 4h16v12l-8 4-8-4z"/><circle cx="24" cy="31" r="12"/><circle cx="24" cy="31" r="8"/><path d="M24 26l1.6 3.4 3.6.4-2.7 2.4.8 3.6-3.3-1.9-3.3 1.9.8-3.6-2.7-2.4 3.6-.4z"/></svg>
  </div>
  <div class="icon-badge" style="left:785px;top:527px">
    <svg viewBox="0 0 48 48"><path d="M24 40V22"/><path d="M24 26c-2-8-10-12-18-10 2 8 10 12 18 10z"/><path d="M24 22c2-10 10-14 20-14-2 10-10 16-20 14z"/><path d="M8 42c4-4 12-6 16-4 4-2 12 0 16 4z"/></svg>
  </div>

  <!-- Row one cards -->
  <section class="card" style="left:37px;top:239px;width:207px;height:274px">
    <h2 class="card-title">Life Balance</h2>
    <ul class="card-list">
      <li>VALMIRA Day Leave. An extra day of at Christmas</li>
      <li>BIRTHDAY Leave. A paid day off on your birthday</li>
      <li>A day off every month as Time in Lieu</li>
      <li>4 weeks Annual Leave</li>
      <li>Genereous Personal Leave</li>
      <li>Support for parental leave for the birth or adoption of a child</li>
      <li>Flexible work arrangements</li>
    </ul>
  </section>

  <section class="card" style="left:264px;top:239px;width:210px;height:245px">
    <h2 class="card-title">Wellbeing</h2>
    <ul class="card-list">
      <li>Up to $450 per year to spend on Wellbeing services such as gym or yoga memberships</li>
      <li>Free counselling services 24x7 via our Employee Assistance Program</li>
      <li>Discount private health insurance</li>
      <li>WHS policies which suppor a safe, inclusive work place</li>
    </ul>
  </section>

  <section class="card" style="left:497px;top:237px;width:210px;height:270px">
    <h2 class="card-title">Career Growth<br>&amp;Professional<br>Development</h2>
    <ul class="card-list">
      <li>Ongoing internal training and development opportunities</li>
      <li>External srudy support &amp; study leave</li>
      <li>Access to the tools and technology to do your job well</li>
      <li>Career advancement opportunities</li>
      <li>Internal job vacancy listing</li>
    </ul>
  </section>

  <section class="card" style="left:730px;top:246px;width:208px;height:216px">
    <h2 class="card-title">Remuneration<br>&amp; Salary Packaging</h2>
    <ul class="card-list">
      <li>Competetive salary</li>
      <li>Ability to salary package up to $15,900 and reduce your tax. Package rent, home loans, child care and much more</li>
      <li>Salary package up to $2,650 on meal entertainment and holiday accommodation</li>
    </ul>
  </section>

  <!-- Row two cards -->
  <section class="card" style="left:35px;top:651px;width:209px;height:185px">
    <h2 class="card-title">Diversity &amp; Inclusion</h2>
    <ul class="card-list">
      <li>An inclusive and diverse culture where different backgounds, experiences and perspectives are valued</li>
      <li>Gender diversity. Over 50% of our workforce and our leaders are female</li>
    </ul>
  </section>

  <section class="card" style="left:262px;top:649px;width:209px;height:227px">
    <h2 class="card-title">Benefits</h2>
    <ul class="card-list">
      <li>Discounted vouchers for Grocella, Fresh Lane, Volt Audio, Reelhouse, Cellar Row, Homeway, Trailpoint and many others via Paywell e-wallet</li>
      <li>A range of other employee discounts are also available, including access to discounted bankin and finance, vehicle purchasing, leasing and hotel accomodation</li>
    </ul>
  </section>

  <section class="card" style="left:497px;top:651px;width:209px;height:132px">
    <h2 class="card-title">Recognition</h2>
    <ul class="card-list">
      <li>We celebrate our people forreaching service milestones</li>
      <li>Team &amp; individual recognition for high performance</li>
    </ul>
  </section>

  <section class="card" style="left:730px;top:650px;width:208px;height:221px">
    <h2 class="card-title">Contributing to<br>Community</h2>
    <ul class="card-list">
      <li>Team involvement in local charity and community events</li>
      <li>Participation in VALMIRA's 1000 Jobs in 100 days</li>
      <li>Strong relationships and connection with Indigenous Communities in support of Indigenous Emplyment</li>
    </ul>
  </section>
</main>
</body>
</html>
```